WebDesign | Financial Services Firm - Risk Mitigation

We are a professional services consulting firm that specializes in high net worth individuals over $25,000,000, executives C-suite and above, closely held businesses owners, family offices and highly compensated employees.

Our focus is on risk mitigation and tax efficient strategies. Our clients take their risk on themselves and have a proven track record generating wealth. Our directive is to preserve and protect the wealth they’ve already created.

Our company Harbor Crest Advisory is geared around five directives of asset protection:
1) Legal Structuring
2) Leverage & Financing
3) Risk Management - Asset Protection & Insurance, Trustee Work
4) Asset Management & Investing - Under www.tqlvalemark.com
5) Tax Efficient Strategies

Our Company Mark is a Pentagon with a key in the middle. A pentagon is the most efficient defensive structure. Each point of a pentagon is equal distance front every point . Each side provides support to another and works together, which is the key to our clients success.

Our key colors are blue, black and silver.

We ‘re located in the Pacific Northwest with bi coastal and international clients. We have fewer, higher net worth clients and provide exceptional customer service. We do not do social media.

We'll need the following pages:
-Front Landing Page.
Front page has to have link to hbportal.docuvaultix.com for logging into secure site.
- Contact & About Us Page
- Our Team Page
- Five Sides of Wealth Management
> Legal & Business Structuring
> Leverage & Financing
> Risk Management & Asset Protection.
> Asset Management and Investing - Will link to TQL (won't be turned on for a few months)
> Tax Efficient Strategies.

Industry/Entity Type

Financial Service

Coding

Coded - Design and coding required

Number of Pages Required

5+ page

Font styles to use
Sans Serif

Colors
0555a3

Requirements
Must have
• Our key colors are blue, black and silver.

-Front Landing Page.
- Contact & About Us Page
- Our Team Page
> Leverage & Financing
Nice to have
• I have attached images that have been purchased for use on the webpage. Us or not.

location page: 847 W Alder Ln, Suite 412, Lake Oswego, OR 97035
Should not have
• lots of color.

```html
<!DOCTYPE html>
<html lang="en">
<head>
<meta charset="utf-8">
<title>Harbor Crest Advisory — About</title>
<link rel="stylesheet" href="https://fonts.googleapis.com/css2?family=Poppins:wght@300;400;500&family=Cinzel:wght@400;500&family=Libre+Baskerville:wght@400;700&display=swap">
<style>
  :root {
    --navy: #16335f;
    --brand-blue: #0555a3;
    --link-blue: #1577c6;
    --cyan: #12bdf0;
    --text-grey: #6b6b6b;
    --footer-bg: #141414;
    --footer-text: #9a9a9a;
    --white: #ffffff;
  }
  * { box-sizing: border-box; margin: 0; padding: 0; }
  html, body { width: 1200px; height: 2369px; overflow: hidden; background: var(--white); }
  body { position: relative; font-family: "Poppins", sans-serif; color: var(--text-grey); }
  .abs { position: absolute; }

  .hero {
    left: 0; top: 0; width: 1200px; height: 465px;
    background: linear-gradient(100deg, #2f73a9 0%, #1f5f9c 35%, #18589a 65%, #1d5d97 100%);
  }
  .hero-name {
    left: 560px; top: 210px; width: 420px; text-align: center;
    font-family: "Poppins", sans-serif; font-weight: 300; font-size: 40px;
    letter-spacing: 6px; color: #8fb6d8; text-transform: uppercase; line-height: 1.2;
  }
  .story-photo {
    left: 138px; top: 233px; width: 353px; height: 483px;
    background: linear-gradient(160deg, #e9ecef 0%, #cfd3d6 40%, #4c5158 70%, #d9d9d6 100%);
    box-shadow: 0 6px 14px rgba(0,0,0,.18);
  }
  .conversation { left: 138px; top: 730px; }
  .conversation .title { font-size: 11px; font-weight: 500; color: var(--link-blue); }
  .conversation .sub { font-size: 9px; color: #333; margin-top: 6px; display: flex; align-items: center; gap: 5px; }

  .story { left: 549px; top: 545px; width: 452px; }
  .story h2 { font-weight: 500; font-size: 26px; color: var(--navy); margin-left: 1px; margin-bottom: 14px; }
  .story p { font-size: 10.4px; line-height: 18px; margin-bottom: 11px; }

  .principles-title { left: 201px; top: 898px; font-weight: 500; font-size: 27px; color: var(--navy); }
  .principle { top: 979px; width: 170px; }
  .principle svg { display: block; height: 44px; }
  .principle h3 { margin-top: 15px; font-weight: 500; font-size: 14px; color: var(--link-blue); }
  .principle p { margin-top: 6px; font-size: 10.4px; line-height: 18px; }

  .band { left: 0; top: 1179px; width: 1200px; height: 83px; background: var(--cyan); }
  .band-text { left: 201px; top: 1210px; width: 545px; font-size: 12.3px; color: var(--white); white-space: nowrap; }
  .band-button {
    left: 762px; top: 1205px; width: 150px; height: 30px; border: 1px solid var(--white);
    border-radius: 15px; color: var(--white); font-family: "Libre Baskerville", serif;
    font-size: 9.5px; display: flex; align-items: center; justify-content: center; letter-spacing: .4px;
  }

  .contact-shape { left: 0; top: 1320px; }
  .contact-kicker {
    left: 0; top: 1622px; width: 1200px; text-align: center; font-family: "Cinzel", serif;
    font-size: 10px; letter-spacing: 2.4px; color: #e8e8e8;
  }
  .contact-title {
    left: 0; top: 1646px; width: 1200px; text-align: center; font-family: "Cinzel", serif;
    font-size: 31px; letter-spacing: 3px; color: var(--white);
  }
  .field {
    background: var(--white); font-size: 8.5px; color: #555; padding-left: 20px;
    display: flex; align-items: center; height: 37px; width: 242px;
  }
  .field.message { align-items: flex-start; padding-top: 14px; width: 500px; height: 74px; }
  .select-caret {
    left: 591px; top: 1776px; width: 17px; height: 37px; background: var(--white);
    display: flex; align-items: center; justify-content: center;
  }
  .submit {
    left: 541px; top: 1943px; width: 118px; height: 28px; border-radius: 14px; background: var(--cyan);
    color: var(--white); font-size: 8.5px; font-weight: 500; letter-spacing: 1px;
    display: flex; align-items: center; justify-content: center;
  }

  .footer { left: 0; top: 2052px; width: 1200px; height: 317px; background: var(--footer-bg); }
  .footer-col { top: 2097px; }
  .footer-col h4 {
    font-family: "Libre Baskerville", serif; font-weight: 700; font-size: 11.5px; letter-spacing: .9px;
    color: #e6e6e6; margin-bottom: 20px; white-space: nowrap;
  }
  .footer-col p { font-size: 10px; line-height: 18px; color: var(--footer-text); }
  .footer-col ul { list-style: none; }
  .footer-col li { font-size: 10px; color: var(--footer-text); line-height: 23.6px; }
  .newsletter-input {
    left: 794px; top: 2186px; width: 190px; height: 27px; background: var(--white);
    font-size: 7px; color: #aaa; padding-left: 10px; display: flex; align-items: center;
  }
  .newsletter-button {
    left: 970px; top: 2184px; width: 30px; height: 30px; border-radius: 50%;
    background: linear-gradient(135deg, #1aa9e8, #0555a3); display: flex; align-items: center; justify-content: center;
  }
  .copyright { left: 201px; top: 2325px; font-size: 9.5px; color: var(--footer-text); }
  .copyright strong { font-weight: 400; color: var(--white); margin-left: 4px; }
  .legal { left: 802px; top: 2327px; width: 198px; text-align: right; font-size: 8.5px; color: var(--footer-text); white-space: nowrap; }
</style>
</head>
<body>

  <div class="abs hero" role="img" aria-label="Office lobby with company name on a blue wall and green plants"></div>
  <div class="abs hero-name">Harbor Crest Advisory</div>

  <div class="abs story-photo" role="img" aria-label="Two business advisors reviewing a tablet at a table"></div>
  <div class="abs conversation">
    <div class="title">Start A Conversation</div>
    <div class="sub">Talk To Us
      <svg width="12" height="8" viewBox="0 0 12 8"><path d="M0 4h11M8 1l3 3-3 3" fill="none" stroke="#12bdf0" stroke-width="1"/></svg>
    </div>
  </div>

  <section class="abs story">
    <h2>Our Story</h2>
    <p>Lorem ipsum dolor sit amet, consectetuer adipiscing elit, sed diam nonummy nibh euismod tincidunt ut laoreet dolore magna aliquam erat volutpat. Ut wisi enim ad minim veniam, quis nostrud exerci tation ullamcorper suscipit lobortis nisl ut aliquip ex ea commodo consequat. Duis autem vel eum iriure dolor in hendrerit in vulputate velit esse molestie consequat, vel illum dolore eu feugiat nulla facilisis at vero eros et accumsan et iusto odio dignissim qui blandit praesent luptatum zzril delenit augue duis dolore te feugait nulla facilisi.</p>
    <p>commodo consequat. Duis autem vel eum iriure dolor in hendrerit in vulputate velit esse molestie consequat, vel illum dolore eu feugiat nulla facilisis at vero eros et accumsan et iusto odio dignissim qui blandit praesent luptatum zzril delenit augue duis dolore te feugait nulla facilisi.</p>
  </section>

  <h2 class="abs principles-title">Our Guiding Principles</h2>

  <div class="abs principle" style="left:201px">
    <svg width="42" height="44" viewBox="0 0 42 44" fill="none" stroke="#1577c6" stroke-width="1.6">
      <circle cx="27" cy="13" r="8"/><circle cx="27" cy="13" r="11" stroke-dasharray="3 3"/>
      <path d="M23 13l3 3 5-6"/><path d="M1 32h8l7 3h9c2 0 2 3 0 3h-8M9 41l9 1 20-9c2-1 1-4-1-3l-10 4"/><path d="M1 29v13"/>
    </svg>
    <h3>Efficient</h3>
    <p>Lorem ipsum dolor sit amet, consectetuer adipiscing elit.</p>
  </div>
  <div class="abs principle" style="left:421px">
    <svg width="48" height="44" viewBox="0 0 48 44" fill="none" stroke="#1577c6" stroke-width="1.6">
      <path d="M20 2c-10 0-18 8-18 19s8 20 18 20"/><path d="M14 20h6v20h-6zM20 22l7-10c2-4 6-3 6 1l-1 7h10c3 0 4 3 2 5 2 1 2 4 0 5 1 2 0 4-2 4 1 2 0 5-3 5H20"/>
    </svg>
    <h3>Reliable</h3>
    <p>Lorem ipsum dolor sit amet, consectetuer adipiscing elit.</p>
  </div>
  <div class="abs principle" style="left:642px">
    <svg width="40" height="44" viewBox="0 0 40 44" fill="none" stroke="#1577c6" stroke-width="1.6">
      <path d="M20 2l16 6v12c0 11-7 18-16 22C11 38 4 31 4 20V8z"/><path d="M20 7l11 4v9c0 8-5 13-11 16-6-3-11-8-11-16v-9z"/>
      <rect x="14" y="19" width="12" height="9"/><path d="M16 19v-3a4 4 0 0 1 8 0v3"/>
    </svg>
    <h3>Protect</h3>
    <p>Lorem ipsum dolor sit amet, consectetuer adipiscing elit.</p>
  </div>
  <div class="abs principle" style="left:863px">
    <svg width="46" height="44" viewBox="0 0 46 44" fill="none" stroke="#1577c6" stroke-width="1.6">
      <rect x="2" y="30" width="7" height="12"/><rect x="13" y="24" width="7" height="18"/><rect x="24" y="18" width="7" height="24"/><rect x="35" y="12" width="7" height="30"/>
      <path d="M4 22l12-8 6 3 14-12M31 4h6v6"/>
    </svg>
    <h3>Grow</h3>
    <p>Lorem ipsum dolor sit amet, consectetuer adipiscing elit.</p>
  </div>

  <div class="abs band"></div>
  <div class="abs band-text">Our company Harbor Crest Advisory is geared around five directives of asset protection</div>
  <div class="abs band-button">View Our Strategies</div>

  <svg class="abs contact-shape" width="1200" height="740" viewBox="0 1320 1200 740" role="img" aria-label="Evening view of a timber-framed lodge entrance">
    <defs>
      <linearGradient id="lodge" x1="0" y1="0" x2="0" y2="1">
        <stop offset="0" stop-color="#3c4049"/>
        <stop offset=".45" stop-color="#2e2a27"/>
        <stop offset=".75" stop-color="#3a2e24"/>
        <stop offset="1" stop-color="#2a2622"/>
      </linearGradient>
    </defs>
    <polygon points="599,1324 1167,1735 1065,2052 136,2052 33,1735" fill="url(#lodge)"/>
  </svg>

  <div class="abs contact-kicker">Drop us a line and we will get back to you.</div>
  <div class="abs contact-title">Get Wealth Protection Now!</div>

  <div class="abs field" style="left:350px; top:1719px">Name</div>
  <div class="abs field" style="left:608px; top:1719px">Email</div>
  <div class="abs field" style="left:350px; top:1776px">Select Your Strategy</div>
  <div class="abs select-caret">
    <svg width="7" height="5" viewBox="0 0 7 5"><path d="M.5 .5l3 3 3-3" fill="none" stroke="#333" stroke-width="1.2"/></svg>
  </div>
  <div class="abs field" style="left:608px; top:1776px">Phone</div>
  <div class="abs field message" style="left:350px; top:1831px">Message</div>
  <div class="abs submit">CONTACT US</div>

  <footer class="abs footer"></footer>
  <div class="abs footer-col" style="left:201px; width:165px">
    <h4>ABOUT US</h4>
    <p>Lorem ipsum dolor sit dolor sit an amet, consectetur adipiscing elit, dolor sed do eiusmod tempor incididunt ut labore.</p>
  </div>
  <div class="abs footer-col" style="left:423px">
    <h4>QUICK LINK</h4>
    <ul><li>Home</li><li>About</li><li>Strategies</li><li>Team</li><li>Contact Us</li></ul>
  </div>
  <div class="abs footer-col" style="left:579px">
    <h4>STRATEGIES</h4>
    <ul><li>Legal Structuring</li><li>Leverage &amp; Financing</li><li>Risk Management</li><li>Asset Management &amp; Investing</li><li>Tax Efficient Strategies</li></ul>
  </div>
  <div class="abs footer-col" style="left:794px; width:210px">
    <h4>SUBSCRIBE TO NEWSLETTERS</h4>
    <p>Lorem ipsum dolor sit amet, coctetur dipiscing elit, sed do eiuod tempor.</p>
  </div>
  <div class="abs newsletter-input">Your Email</div>
  <div class="abs newsletter-button">
    <svg width="12" height="8" viewBox="0 0 12 8"><path d="M0 4h11M8 1l3 3-3 3" fill="none" stroke="#fff" stroke-width="1"/></svg>
  </div>

  <div class="abs copyright">© 2021 <strong>HARBOR CREST ADVISORY</strong></div>
  <div class="abs legal">Privacy Policy &nbsp;|&nbsp; Terms and Conditions</div>

</body>
</html>
```